Mental Health Awareness License Plates

Below is the sample format I will need. That of a plain license plate w/o frame
*refer to image with name Licence wo Frame*
Delete Frame
Replace QR Code with “MO”
Replace 2025 sticker with “ YR
Use License Plate font (attached)
On Ribbon, keep the green background
The California front leg, needs to be gradated like a sunset and retain shape of CA
Palm trees sharpened
I need the files in a format that can be used on a website, printed or made into a poster.
One file that reads SAMPLE, one version that reads “NEWPLA8”d
The finished product should look like a license plate as shown in the example
*refer to image name finished product*
I want to clarify what we are looking for. The license plate design has been approved by the state, but we need a high res version of it in multiple file formats. The most important change we are looking for is to the ribbon. The palm trees against the sunset are fuzzy, we need those placed in front of an sunset on the front leg of the ribbon. The rear leg needs to remain green (mental health color). I hope this help clarify our design need.

```html
<!DOCTYPE html>
<html lang="en">
<head>
<meta charset="utf-8">
<title>Mental Health Awareness License Plates</title>
<link rel="stylesheet" href="https://fonts.googleapis.com/css2?family=Big+Shoulders+Display:wght@700&family=Josefin+Sans:wght@600&display=swap">
<style>
  :root {
    --mint: #b2f7ea;
    --navy: #234a6a;
    --state-red: #e0454a;
    --ribbon-green: #3f9a3a;
    --ribbon-light: #8cc63f;
    --sunset-orange: #f2a33a;
    --page: #ffffff;
    --shadow: rgba(0, 0, 0, 0.35);
  }
  html, body {
    margin: 0;
    padding: 0;
    width: 1200px;
    height: 1200px;
    overflow: hidden;
    background: var(--page);
  }
  .canvas {
    position: relative;
    width: 1200px;
    height: 1200px;
  }
  .plate {
    position: absolute;
    width: 648px;
    height: 324px;
    filter: drop-shadow(5px 5px 3px var(--shadow));
  }
  .plate--light { left: 276px; top: 223px; }
  .plate--dark { left: 274px; top: 654px; }
  .plate svg { display: block; width: 648px; height: 324px; }
  .state-name {
    font-family: "Josefin Sans", sans-serif;
    font-weight: 600;
    font-size: 50px;
  }
  .plate-number {
    font-family: "Big Shoulders Display", sans-serif;
    font-weight: 700;
    font-size: 180px;
  }
  .cause-line {
    font-family: "Josefin Sans", sans-serif;
    font-weight: 600;
    font-size: 19px;
    letter-spacing: 5px;
  }
</style>
</head>
<body>
<main class="canvas">

  <section class="plate plate--light" aria-label="Light license plate, NEWPL8">
    <svg viewBox="0 0 648 324" xmlns="http://www.w3.org/2000/svg">
      <defs>
        <linearGradient id="emblem-light" x1="0" y1="0" x2="1" y2="1">
          <stop offset="0" stop-color="var(--ribbon-light)"/>
          <stop offset="0.45" stop-color="var(--sunset-orange)"/>
          <stop offset="1" stop-color="var(--ribbon-green)"/>
        </linearGradient>
      </defs>
      <rect class="plate-base" width="648" height="324" fill="var(--mint)"/>
      <rect class="sticker-slot" x="49" y="39" width="85" height="54" fill="none" stroke="var(--navy)" stroke-width="3"/>
      <rect class="sticker-slot" x="517" y="39" width="85" height="54" fill="none" stroke="var(--navy)" stroke-width="3"/>
      <text class="state-name" x="332" y="86" text-anchor="middle" fill="var(--state-red)" textLength="310" lengthAdjust="spacingAndGlyphs">California</text>
      <rect class="emblem" x="34" y="118" width="166" height="154" rx="8" fill="url(#emblem-light)" opacity="0.85"
            role="img" aria-label="Green awareness ribbon whose front leg is the shape of California in a sunset gradient, with palm trees in front"/>
      <text class="plate-number" x="216" y="265" fill="var(--navy)" textLength="382" lengthAdjust="spacingAndGlyphs">NEWPL8</text>
      <text class="cause-line" x="106" y="305" fill="var(--navy)" textLength="430" lengthAdjust="spacing">MENTAL HEALTH AWARENESS</text>
    </svg>
  </section>

  <section class="plate plate--dark" aria-label="Dark license plate, NEWPL8">
    <svg viewBox="0 0 648 324" xmlns="http://www.w3.org/2000/svg">
      <defs>
        <linearGradient id="emblem-dark" x1="0" y1="0" x2="1" y2="1">
          <stop offset="0" stop-color="var(--ribbon-light)"/>
          <stop offset="0.45" stop-color="var(--sunset-orange)"/>
          <stop offset="1" stop-color="var(--ribbon-green)"/>
        </linearGradient>
      </defs>
      <rect class="plate-base" width="648" height="324" fill="var(--navy)"/>
      <rect class="sticker-slot" x="49" y="39" width="85" height="54" fill="none" stroke="var(--mint)" stroke-width="3"/>
      <rect class="sticker-slot" x="517" y="39" width="85" height="54" fill="none" stroke="var(--mint)" stroke-width="3"/>
      <text class="state-name" x="332" y="86" text-anchor="middle" fill="var(--mint)" textLength="310" lengthAdjust="spacingAndGlyphs">California</text>
      <rect class="emblem" x="34" y="118" width="166" height="154" rx="8" fill="url(#emblem-dark)" opacity="0.85"
            role="img" aria-label="Green awareness ribbon whose front leg is the shape of California in a sunset gradient, with palm trees in front"/>
      <rect class="number-panel" x="210" y="127" width="398" height="145" fill="var(--mint)"/>
      <text class="plate-number" x="218" y="264" fill="var(--navy)" textLength="380" lengthAdjust="spacingAndGlyphs">NEWPL8</text>
      <text class="cause-line" x="106" y="305" fill="var(--mint)" textLength="430" lengthAdjust="spacing">MENTAL HEALTH AWARENESS</text>
    </svg>
  </section>

</main>
</body>
</html>
```